GUARANTEED! Simple website for independent event planner and consultant...

I need a website that is no more than 5 or 6 pages to illustrate who I am and what I can offer to groups who book hotels for meetings and conferences. I have 20 years of experience planning meetings within hotels and I am now ready to go out on my own and help clients choose venues, negotiate contracts and plan effective meetings. I will focus on clients planning meetings in the mountains of Colorado but I am willing to travel as well. I want to work with a person who is collaborative and can direct me on what they need to move the project along quickly. I already have my logo, a hosting site and work e-mail address. Also, I recently hired a photographer to do head shots. Lastly, it important for me to be able to talk on the phone or skype with this person, as needed and I must be able to make changes to my site down the road when necessary...

Target Market(s)

Corporate Groups

Industry/Entity Type

Event Planning

Coding

Coded - Design and coding required

Number of Pages Required

5+ page

Font styles to use
Sans Serif

Requirements
Must have
• About me page, event planning services offered page, task force and consulting work page, testimonials page, page for blogs, page to contact me/request a proposal. May need advice on what else I need...
Nice to have
• I want it to look sharp and professional. I want people to look at my site and know immediately that they can trust me and the work I can do.
• I don't want it to look like it is over the top as I am not a HUGE company but I do want it to be professional and easy to view and navigate.
Should not have
• Bright colors
• My logo is bright orange and black. I have also used dark grey and orange. See below:
• Orange:
• C = 0
• M = 64
• Y = 100
• K = 0
• Gray:
• C = 67
• M = 60
• Y = 59
• K = 45
• Font: Gotham Book and Gotham Bold

```html
<!DOCTYPE html>
<html lang="en">
<head>
<meta charset="utf-8">
<title>Harlow Event Management</title>
<link rel="stylesheet" href="https://fonts.googleapis.com/css2?family=Montserrat:wght@300;400;500;700&display=swap">
<style>
  :root {
    --orange: #f47b20;
    --charcoal: #3a3a3c;
    --ink: #2b2b2d;
    --white: #ffffff;
    --rule: #c9ccd1;
    --steel-dark: #1d2a3a;
    --steel-mid: #4d6580;
    --steel-light: #b9c7d6;
  }
  * { box-sizing: border-box; margin: 0; padding: 0; }
  html, body { width: 1200px; height: 769px; overflow: hidden; }
  body { font-family: "Montserrat", sans-serif; color: var(--ink); background: var(--white); }

  .page { position: relative; width: 1200px; height: 769px; overflow: hidden; }

  .hero-photo {
    position: absolute; inset: 0;
    background:
      radial-gradient(ellipse at 62% 45%, rgba(185,199,214,.55), rgba(185,199,214,0) 55%),
      linear-gradient(180deg, var(--steel-light) 0%, var(--steel-mid) 40%, var(--steel-dark) 100%);
  }
  .header-fade {
    position: absolute; left: 0; top: 0; width: 100%; height: 260px;
    background: linear-gradient(180deg, rgba(255,255,255,1) 0%, rgba(255,255,255,.96) 55%, rgba(255,255,255,.6) 78%, rgba(255,255,255,0) 100%);
  }

  .brand { position: absolute; left: 21px; top: 33px; display: flex; align-items: center; gap: 12px; }
  .brand-mark { width: 22px; height: 22px; background: var(--orange); }
  .brand-name { color: var(--orange); font-weight: 700; line-height: 1; }
  .brand-name .primary { display: block; font-size: 52px; letter-spacing: 1px; }
  .brand-name .secondary { display: block; font-size: 15.5px; letter-spacing: 1.4px; margin-top: 6px; }

  .social { position: absolute; top: 36px; left: 839px; display: flex; gap: 11px; }
  .social-square { width: 36px; height: 36px; background: var(--orange); }

  .call-box {
    position: absolute; top: 36px; left: 981px; width: 185px; height: 35px;
    border: 1px solid var(--orange); background: var(--white);
    display: flex; align-items: center; justify-content: center; gap: 6px;
    font-size: 13.5px; color: var(--ink);
  }
  .call-box strong { font-weight: 700; }
  .call-box svg { margin-left: 4px; }

  .email { position: absolute; top: 81px; right: 34px; font-size: 13.5px; color: var(--ink); display: flex; align-items: center; gap: 6px; }

  .main-nav { position: absolute; top: 158px; right: 34px; display: flex; gap: 26px; }
  .main-nav a { position: relative; font-size: 15.5px; color: var(--ink); text-decoration: none; text-transform: uppercase; letter-spacing: .2px; }
  .main-nav a.is-active::after {
    content: ""; position: absolute; left: -6px; right: -6px; top: 36px; height: 2px; background: var(--orange);
  }
  .nav-rule { position: absolute; left: 21px; right: 34px; top: 195px; height: 1px; background: var(--rule); }

  .hero-text { position: absolute; left: 0; width: 100%; top: 388px; text-align: center; color: var(--white); }
  .hero-title { font-weight: 300; font-size: 46px; letter-spacing: 1px; line-height: 1; text-shadow: 0 1px 6px rgba(0,0,0,.35); }
  .hero-sub {
    margin-top: 14px; font-weight: 700; font-size: 21.5px; line-height: 1.5; text-transform: uppercase; letter-spacing: .3px;
    text-shadow: 0 2px 6px rgba(0,0,0,.7);
  }

  .feature-tile { position: absolute; top: 538px; width: 168px; height: 178px; }
  .feature-tile .frame { position: absolute; left: 24px; top: 0; width: 143px; height: 178px; border: 5px solid var(--orange); }
  .feature-tile .photo { position: absolute; left: 0; top: 11px; width: 155px; height: 152px; border: 4px solid #4a4f57; }
  .tile-1 { left: 369px; }
  .tile-2 { left: 602px; }
  .tile-3 { left: 834px; }
  .photo-keynote { background: linear-gradient(180deg, #dfe6ee 0%, #b8c6d6 45%, #3b4656 100%); }
  .photo-dining { background: linear-gradient(160deg, #6e4a34 0%, #9a6d4c 40%, #3c2a20 100%); }
  .photo-seminar { background: linear-gradient(180deg, #b65d2f 0%, #d98a4e 40%, #3a2a28 100%); }
</style>
</head>
<body>
<div class="page">
  <div class="hero-photo" role="img" aria-label="Photo of an empty corporate boardroom with a long polished table and leather chairs"></div>
  <div class="header-fade"></div>

  <header>
    <div class="brand">
      <div class="brand-name">
        <span class="primary">HARLOW</span>
        <span class="secondary">EVENT MANAGEMENT</span>
      </div>
      <span class="brand-mark"></span>
    </div>

    <div class="social" aria-label="Social links">
      <span class="social-square"></span>
      <span class="social-square"></span>
      <span class="social-square"></span>
    </div>

    <div class="call-box">Call: <strong>970.555.0148</strong>
      <svg width="11" height="7" viewBox="0 0 11 7"><path d="M1 1l4.5 4.5L10 1" fill="none" stroke="#2b2b2d" stroke-width="1.3"/></svg>
    </div>

    <div class="email">
      <svg width="12" height="9" viewBox="0 0 12 9"><rect x=".5" y=".5" width="11" height="8" fill="none" stroke="#2b2b2d"/><path d="M.5 .5L6 5l5.5-4.5" fill="none" stroke="#2b2b2d"/></svg>
      jane@harloweventmanagement.com
    </div>

    <nav class="main-nav">
      <a class="is-active" href="#">Home</a>
      <a href="#">About Me</a>
      <a href="#">Services</a>
      <a href="#">Task Force &amp; Consulting</a>
      <a href="#">Testimonials</a>
      <a href="#">Blog</a>
      <a href="#">Contact Me</a>
    </nav>
    <div class="nav-rule"></div>
  </header>

  <section class="hero-text">
    <h1 class="hero-title">HARLOW EVENT MANAGEMENT</h1>
    <p class="hero-sub">Specializes in event management for associations, corporations, not for profit<br>companies and personal social events of all sizes in the state of Colorado.</p>
  </section>

  <div class="feature-tile tile-1">
    <div class="frame"></div>
    <div class="photo photo-keynote" role="img" aria-label="Photo of a speaker presenting to a seated audience"></div>
  </div>
  <div class="feature-tile tile-2">
    <div class="frame"></div>
    <div class="photo photo-dining" role="img" aria-label="Photo of wine glasses and plated food on a banquet table"></div>
  </div>
  <div class="feature-tile tile-3">
    <div class="frame"></div>
    <div class="photo photo-seminar" role="img" aria-label="Photo of a presenter at a seminar with a projected chart"></div>
  </div>
</div>
</body>
</html>
```